Finance Product Agency Business Card Design

We're an agency that provides products (service contracts, gap insurance, tire and wheel, etc) and support to dealership finance departments. We specialize in training finance producers to maximize their potential and also keep them up to date on the ever changing compliance and legal landscape. I'll attach an image of our logo, excited to see what you all come up with. Would also be interested in discussing our new website design with the winner.

Target Market(s)

auto dealerships

Industry/Entity Type

Business

Contact Information for Business Card

Dale Hoskirk
Phone 517.364.2908
Fax 877.245.3196
email Dale.Hoskirk@brightlanecoverage.com

Requirements
Must have
• basic contact information
Nice to have
• looking for something professional but modern

```html
<!DOCTYPE html>
<html lang="en">
<head>
<meta charset="utf-8">
<title>Brightlane Coverage – Business Card</title>
<link rel="stylesheet" href="https://fonts.googleapis.com/css2?family=Roboto:wght@400;700&display=swap">
<style>
  :root {
    --stage: #2e2e30;
    --paper: #ffffff;
    --ink: #1d2a33;
    --ink-soft: #3c4a54;
    --teal: #2f5568;
    --teal-deep: #20394a;
    --night: #0b0d10;
  }
  * { margin: 0; padding: 0; box-sizing: border-box; }
  html, body {
    width: 1200px; height: 716px; overflow: hidden;
    background: var(--stage);
    font-family: "Roboto", Arial, sans-serif;
  }
  .stage {
    position: relative; width: 1200px; height: 716px;
    display: flex; align-items: center; justify-content: center; gap: 50px;
  }
  .card {
    position: relative; width: 525px; height: 300px; overflow: hidden;
    box-shadow: 0 14px 30px rgba(0,0,0,.45);
  }

  /* Front */
  .card-front { background: var(--paper); }
  .front-band {
    position: absolute; left: 0; right: 0; bottom: 0; height: 92px;
    background: linear-gradient(180deg, var(--teal) 0%, var(--teal-deep) 35%, var(--night) 100%);
  }
  .band-notch { position: absolute; left: 74px; bottom: 66px; }
  .holder { position: absolute; left: 28px; top: 26px; color: var(--ink); }
  .holder-name { font-size: 17px; font-weight: 700; }
  .holder-role { font-size: 10px; margin-top: 3px; color: var(--ink-soft); }
  .contact-list {
    position: absolute; left: 28px; top: 104px; list-style: none;
    color: var(--ink-soft); font-size: 11px;
  }
  .contact-item { display: flex; align-items: center; gap: 8px; height: 17px; }
  .contact-icon { width: 14px; height: 14px; flex: none; }
  .front-brand {
    position: absolute; right: 34px; top: 82px;
    display: flex; align-items: center; gap: 10px;
  }
  .brand-dot { width: 34px; height: 34px; border-radius: 50%; background: var(--teal); }
  .brand-name {
    font-size: 26px; font-weight: 700; letter-spacing: .5px; line-height: 1;
    color: var(--teal-deep);
  }

  /* Back */
  .card-back {
    background: linear-gradient(165deg, var(--teal) 0%, var(--teal-deep) 30%, var(--night) 85%);
  }
  .back-brand {
    position: absolute; left: 150px; top: 128px;
    display: flex; align-items: center; gap: 12px;
  }
  .back-brand .brand-dot { background: var(--paper); }
  .back-brand .brand-name { color: var(--paper); font-size: 30px; }
</style>
</head>
<body>
<main class="stage">

  <section class="card card-front" aria-label="Card front">
    <div class="holder">
      <p class="holder-name">Dale Hoskirk</p>
      <p class="holder-role">Director</p>
    </div>

    <ul class="contact-list">
      <li class="contact-item">
        <svg class="contact-icon" viewBox="0 0 14 14" aria-hidden="true">
          <rect width="14" height="14" fill="#2f5568"/>
          <path d="M4 3.2c.6-.4 1.1-.2 1.4.4l.5 1.1c.2.4 0 .8-.3 1l-.4.3c.4.9 1.1 1.7 2 2.1l.3-.4c.3-.3.7-.4 1-.2l1.1.6c.5.3.6.8.3 1.3-.6.9-1.5 1.2-2.5.7C5.6 9.2 4.3 7.8 3.5 6c-.4-1-.2-2.2.5-2.8z" fill="#fff"/>
        </svg>
        517.364.2908
      </li>
      <li class="contact-item">
        <svg class="contact-icon" viewBox="0 0 14 14" aria-hidden="true">
          <rect width="14" height="14" fill="#2f5568"/>
          <rect x="4.5" y="2.5" width="5" height="3" fill="#fff"/>
          <rect x="2.5" y="5.5" width="9" height="4" rx="1" fill="#fff"/>
          <rect x="4.5" y="8.5" width="5" height="3" fill="#fff" stroke="#2f5568" stroke-width=".6"/>
        </svg>
        877.245.3196
      </li>
      <li class="contact-item">
        <svg class="contact-icon" viewBox="0 0 14 14" aria-hidden="true">
          <rect width="14" height="14" fill="#2f5568"/>
          <rect x="2.5" y="4" width="9" height="6" fill="#fff"/>
          <path d="M2.5 4l4.5 3.5L11.5 4" fill="none" stroke="#2f5568" stroke-width=".9"/>
        </svg>
        Dale.Hoskirk@brightlanecoverage.com
      </li>
    </ul>

    <div class="front-brand">
      <span class="brand-dot" aria-hidden="true"></span>
      <span class="brand-name">BRIGHTLANE COVERAGE</span>
    </div>

    <div class="front-band" aria-hidden="true"></div>
    <svg class="band-notch" width="44" height="30" viewBox="0 0 44 30" aria-hidden="true">
      <polygon points="0,0 44,0 22,14" fill="#ffffff"/>
      <polygon points="14,14 20,20 14,26 8,20" fill="#ffffff"/>
      <polygon points="30,14 36,20 30,26 24,20" fill="#ffffff"/>
    </svg>
  </section>

  <section class="card card-back" aria-label="Card back">
    <div class="back-brand">
      <span class="brand-dot" aria-hidden="true"></span>
      <span class="brand-name">BRIGHTLANE COVERAGE</span>
    </div>
  </section>

</main>
</body>
</html>
```